We need UI/UX design for a public, informational website for The Copper Lantern.
The pages, structure, and content scope are already defined. Designers are required to work only on the UI/UX layout of these existing pages, focusing on clarity, hierarchy, spacing, and usability. Do not add, remove, rename, or reinterpret pages or content.
The website is strictly informational only. It must not include accounts, onboarding, payments, custody, escrow administration, marketplaces, dashboards, or any transactional functionality.
Scope of work
Apply UI/UX design to the predefined website pages
Design layout for text, images, notices, and sections
Ensure consistent components and layout patterns across page types
Optimize layouts for long form, compliance focused content
Content writing, page creation, and branding changes are out of scope.
Structure reference
The complete page list, hierarchy, and content definitions are provided in the technical documentation and must be treated as the primary source of truth.
A Figma link is provided only as a light visual reference for page existence and structure:
https://maple-kettle-48203917.plansite.example/
Designers must rely on the documentation for in depth and authoritative reference.
Brand guidelines
The Copper Lantern has existing brand guidelines and official logos, including light and dark versions. These assets will be provided and must be followed exactly. Designers must not redesign, alter, or reinterpret the brand identity.
Look and feel direction
The desired visual direction is inspired by:
https://quorvanta.example/
This reference is provided only to indicate:
Institutional and enterprise tone
Clean, modern typography
Strong hierarchy and generous whitespace
Editorial, content first layouts
Do not copy branding, layouts, components, or assets from the reference site.
Hero section direction
The hero section should follow a similar structural approach to the hero used on https://quorvanta.example/
, meaning:
Strong editorial framing
Clear headline hierarchy
Calm, institutional first impression
However, the background video must be Abu Dhabi focused, not generic or global. The video should visually reflect:
Abu Dhabi skyline or architectural language
Institutional, sovereign, long term infrastructure tone
Clean, slow, cinematic motion
No promotional, marketing, or lifestyle visuals
The hero must remain informational, restrained, and credible. No hype. No calls to invest. No implied participation.
Constraints
One global primary CTA only: “Continue to Brightmoor” (external)
All other interactions must be informational
No visuals or language implying offers, investment, eligibility, or participation
Clear separation between informational content and any external operational platforms
Deliverables
High fidelity UI/UX designs created in Figma, covering:
Desktop layouts
Tablet layouts where relevant
Mobile layouts
Complete Figma file(s) including:
All designed pages defined in the technical documentation
A reusable component library (headers, footers, cards, notice panels, forms, CTAs, typography styles, spacing system)
Clearly defined layout grids, spacing rules, and text styles
Proper use of components and variants, not detached frames
Designs prepared for developer handoff, including:
Clear layer naming and structure
Auto layout where appropriate
Consistent use of styles and components
Responsive behavior demonstrated within Figma
Notes or annotations only where necessary for clarity
No prototypes, interactions, or motion design beyond basic layout states, unless explicitly requested. The focus is static UI/UX clarity, not animation.
A detailed technical specification document and official brand assets will be provided.
Any designs delivered outside Figma, that alter structure or content, or that ignore the defined constraints, boundaries, or tone will be rejected.

```html
<!DOCTYPE html>
<html lang="en">
<head>
<meta charset="UTF-8">
<title>The Copper Lantern — Governance and Project Origination</title>
<link rel="stylesheet" href="https://fonts.googleapis.com/css2?family=Archivo:wght@700;800;900&family=Plus+Jakarta+Sans:wght@400;500;600;700&display=swap">
<style>
:root{
  --ink:#0f1115;
  --body:#4a4f5a;
  --white:#ffffff;
  --purple:#b47cf6;
  --purple-deep:#8c5cf0;
  --blue:#2a9fe0;
  --cyan:#38c6f4;
  --contact:#45e3fe;
  --footer:#000000;
  --card-border:#c8c4f6;
  --hero-top:#4f5f6c;
  --hero-bottom:#2e3b45;
}
*{box-sizing:border-box;margin:0;padding:0}
html,body{width:1200px;height:2796px;overflow:hidden}
body{position:relative;background:var(--white);font-family:"Plus Jakarta Sans",Arial,sans-serif;color:var(--ink)}
.abs{position:absolute}
.heading{font-family:"Archivo",Arial,sans-serif;font-weight:800;text-transform:uppercase;color:var(--ink);line-height:1.25;letter-spacing:-0.2px}
.accent{color:var(--purple)}
.copy{font-size:10.5px;line-height:17.5px;color:var(--body)}
.center{text-align:center}

/* buttons */
.btn{position:absolute;display:flex;align-items:center;justify-content:space-between;gap:10px;height:30px;border-radius:16px;padding:0 4px 0 14px;font-size:10.5px;font-weight:600;text-decoration:none;white-space:nowrap}
.btn--light{background:var(--white);color:var(--ink)}
.btn--dark{background:var(--ink);color:var(--white)}
.btn--outline{border:1px solid rgba(255,255,255,.85);color:var(--white)}
.btn__arrow{flex:none;width:22px;height:22px;border-radius:50%;background:linear-gradient(135deg,var(--cyan),var(--purple-deep));display:flex;align-items:center;justify-content:center}

/* nav */
.brand{display:flex;align-items:center;gap:8px;font-weight:500;color:var(--white);letter-spacing:.6px;text-transform:uppercase;white-space:nowrap}
.brand__dot{width:10px;height:10px;border-radius:50%;background:var(--blue)}
.nav{top:27px;left:331px;display:flex;font-size:10.5px;font-weight:500;color:var(--white);white-space:nowrap}
.nav a{color:var(--white);text-decoration:none;margin-right:32px}
.nav a.is-active{color:#4fb8f5}
.nav .caret{font-size:8px;margin-left:2px}

/* hero */
.hero{top:0;left:0;width:1200px;height:565px;background:linear-gradient(180deg,var(--hero-top) 0%,#5d6d79 40%,var(--hero-bottom) 100%)}
.hero__title{top:200px;left:0;width:1200px;font-size:43px;color:var(--white);letter-spacing:.5px;text-align:center}
.hero__lead{top:259px;left:255px;width:690px;font-size:10.5px;line-height:17px;color:var(--white);text-align:center;font-weight:500}

/* intro */
.intro__title{top:618px;left:112px;font-size:30px}
.intro__copy{top:623px;left:518px;width:530px}

/* role cards */
.roles__title{top:781px;left:0;width:1200px;font-size:30px}
.roles__lead{top:826px;left:270px;width:660px}
.card{position:absolute;top:886px;width:312px;height:253px;background:var(--white);border:1px solid var(--card-border);border-radius:8px;padding:24px 22px 0 24px}
.card__icon{width:52px;height:52px;border:1px solid #a9c8f6;border-radius:6px;display:flex;align-items:center;justify-content:center}
.card__title{font-size:17.5px;margin-top:28px}
.card__desc{font-size:10px;line-height:15.5px;color:var(--body);margin-top:5px;width:260px}
.card__rule{height:1px;background:#cfd3dc;margin-top:9px;width:266px}
.card__list{list-style:none;margin-top:7px}
.card__list li{font-size:10px;line-height:18px;color:var(--body);padding-left:11px;position:relative;white-space:nowrap}
.card__list li::before{content:"";position:absolute;left:0;top:7px;width:5px;height:5px;border-radius:50%;background:var(--purple)}
.card__mark{position:absolute;right:18px;bottom:6px;display:flex;align-items:center;gap:3px;font-size:4.5px;font-weight:600;color:var(--ink);text-transform:uppercase;white-space:nowrap}
.card__mark span{width:6px;height:6px;border-radius:50%;border:1px solid var(--blue)}

/* ecosystem */
.eco__title{top:1204px;left:0;width:1200px;font-size:30px}
.eco__lead{top:1250px;left:270px;width:660px}
.step{position:absolute;width:260px;text-align:center}
.step__title{font-size:17.5px}
.step__desc{font-size:10px;line-height:15px;color:var(--body);margin-top:6px}

/* escrow */
.escrow-bg{top:1560px;left:0;width:1200px;height:640px;background:linear-gradient(180deg,#ffffff 0%,#eef7fe 30%,#f4faff 70%,#ffffff 100%)}
.escrow__title{top:1617px;left:113px;font-size:30px;line-height:42px}
.escrow__copy{top:1706px;left:113px;width:440px}
.overview__frame{top:1609px;left:622px;width:465px;height:203px;border-radius:8px;border:2px solid #9f8ef6;background:var(--white);overflow:hidden}
.overview__head{height:54px;display:flex;align-items:center;justify-content:center;font-size:17.5px;border-bottom:1px solid #cfd3dc}
.overview__row{display:flex;gap:14px;padding:10px 18px 0 18px;height:73px}
.overview__row + .overview__row{border-top:1px solid #cfd3dc}
.overview__icon{flex:none;width:38px;height:38px;border:1px solid #a9c8f6;border-radius:6px;display:flex;align-items:center;justify-content:center;margin-top:4px}
.overview__label{font-size:10.5px;font-weight:700;color:var(--ink);margin-top:3px}
.overview__text{font-size:10px;line-height:15.5px;color:var(--body);margin-top:2px}

/* workflow */
.workflow__media{top:1872px;left:110px;width:439px;height:251px;border-radius:6px;border:3px solid;border-color:#a98cf6 #78c4f6 #78c4f6 #a98cf6;background:linear-gradient(120deg,#e9edf2 0%,#c9d0d8 30%,#f2f3f5 55%,#7a6a5c 80%,#3b2c22 100%)}
.workflow__title{top:1896px;left:611px;font-size:30px;line-height:42px}
.workflow__copy{top:1983px;left:611px;width:445px}

/* contact */
.contact{top:2188px;left:0;width:1200px;height:224px;background:var(--contact)}
.contact__title{top:2234px;left:0;width:1200px;font-size:30px}
.contact__lead{top:2280px;left:290px;width:620px;color:#2d4a55}

/* footer */
.footer{top:2412px;left:0;width:1200px;height:384px;background:var(--footer)}
.footer__about{top:2545px;left:113px;width:180px;font-size:10px;line-height:16.5px;color:#e6e6e6}
.footer__col{position:absolute;top:2477px}
.footer__col h4{font-family:"Archivo",Arial,sans-serif;font-weight:800;font-size:13px;color:var(--white);text-transform:uppercase;margin-bottom:10px}
.footer__col a{display:block;font-size:10px;line-height:20px;color:#e6e6e6;text-decoration:none;white-space:nowrap}
.footer__rule{top:2693px;left:113px;width:974px;height:1px;background:#7a7a7a}
.footer__legal{left:113px;font-size:10px;color:#e6e6e6;white-space:nowrap}
</style>
</head>
<body>

<!-- Hero -->
<section class="hero abs" role="img" aria-label="Abu Dhabi skyline photographed from above at dusk, with towers and the waterfront in muted blue-grey tones"></section>

<svg class="abs" style="top:0;left:0" width="1200" height="600" viewBox="0 0 1200 600" aria-hidden="true">
  <defs>
    <linearGradient id="arcGrad" x1="0" y1="0" x2="1" y2="0">
      <stop offset="0" stop-color="#c39cf8"/>
      <stop offset=".5" stop-color="#a572f4"/>
      <stop offset="1" stop-color="#c39cf8"/>
    </linearGradient>
  </defs>
  <path d="M0 499 Q600 600 1200 499 L1200 600 L0 600 Z" fill="#ffffff"/>
  <path d="M114 530 Q600 620 1086 530 Q600 600 114 530 Z" fill="url(#arcGrad)"/>
</svg>

<header>
  <div class="brand abs" style="top:26px;left:112px;font-size:12px">
    <span class="brand__dot"></span>The Copper Lantern
  </div>
  <nav class="nav abs">
    <a href="#" class="is-active">Home</a>
    <a href="#">Framework <span class="caret">&#8964;</span></a>
    <a href="#">Projects</a>
    <a href="#">Brightmoor</a>
    <a href="#">Insights <span class="caret">&#8964;</span></a>
    <a href="#">Company <span class="caret">&#8964;</span></a>
    <a href="#">Contact <span class="caret">&#8964;</span></a>
  </nav>
  <a class="btn btn--light" href="#" style="top:19px;left:914px;width:173px">Continue to Brightmoor
    <span class="btn__arrow"><svg width="10" height="10" viewBox="0 0 10 10"><path d="M1 5h7M5 2l3 3-3 3" stroke="#fff" stroke-width="1.4" fill="none" stroke-linecap="round"/></svg></span>
  </a>
</header>

<h1 class="heading hero__title abs">The Copper Lantern</h1>
<p class="hero__lead abs">The Copper Lantern is a governance and project origination group. Its purpose is to define structural standards and oversight principles for complex initiatives that may involve multiple parties, staged execution, and long-term accountability.</p>
<a class="btn btn--light" href="#" style="top:316px;left:421px;width:173px">Continue to Brightmoor
  <span class="btn__arrow"><svg width="10" height="10" viewBox="0 0 10 10"><path d="M1 5h7M5 2l3 3-3 3" stroke="#fff" stroke-width="1.4" fill="none" stroke-linecap="round"/></svg></span>
</a>
<a class="btn btn--outline" href="#" style="top:316px;left:606px;width:159px">Learn the Framework
  <span class="btn__arrow"><svg width="10" height="10" viewBox="0 0 10 10"><path d="M1 5h7M5 2l3 3-3 3" stroke="#fff" stroke-width="1.4" fill="none" stroke-linecap="round"/></svg></span>
</a>

<!-- Intro -->
<h2 class="heading intro__title abs">Governance and<br>project <span class="accent">origination</span></h2>
<p class="copy intro__copy abs">Governance in this context refers to the standards that determine how projects are structured and how oversight is described. Origination refers to the initial design and definition of an initiative, including role separation, reporting expectations, and boundary setting before execution begins. The Copper Lantern focuses on these governance-level elements rather than on operating day-to-day workflows.</p>

<!-- Role separation band -->
<svg class="abs" style="top:725px;left:0" width="1200" height="520" viewBox="0 0 1200 520" aria-hidden="true">
  <defs>
    <linearGradient id="bandGrad" x1="0" y1="0" x2="0" y2="1">
      <stop offset="0" stop-color="#cbe7fb"/>
      <stop offset=".55" stop-color="#e4f3fd"/>
      <stop offset="1" stop-color="#ffffff"/>
    </linearGradient>
  </defs>
  <path d="M0 54 Q600 -54 1200 54 L1200 520 L0 520 Z" fill="url(#bandGrad)"/>
</svg>

<h2 class="heading roles__title abs center">Clear role <span class="accent">separation</span></h2>
<p class="copy roles__lead abs center">The ecosystem is designed around clear separation of responsibilities. Governance activities belong at the framework layer. Operational workflows, where available, belong on a separate operating platform designed for process execution and recordkeeping.</p>

<article class="card" style="left:113px">
  <div class="card__icon">
    <svg width="30" height="30" viewBox="0 0 30 30" fill="none" stroke="#8f8cf2" stroke-width="1.3"><path d="M4 11L15 4l11 7z"/><path d="M5 12h20M7 13v10M11 13v10M15 13v10M19 13v10M23 13v10M4 24h22M3 27h24"/></svg>
  </div>
  <h3 class="heading card__title">Governance</h3>
  <p class="card__desc">Governance activities are defined and enforced at the framework level.</p>
  <div class="card__rule"></div>
  <ul class="card__list">
    <li>Defines role separation and accountability concepts</li>
    <li>Sets reporting and transparency expectations</li>
    <li>Does not execute operational workflows</li>
  </ul>
  <div class="card__mark"><span></span>The Copper Lantern</div>
</article>

<article class="card" style="left:444px">
  <div class="card__icon">
    <svg width="32" height="30" viewBox="0 0 32 30" fill="none" stroke="#8f8cf2" stroke-width="1.3"><circle cx="11" cy="18" r="5"/><circle cx="11" cy="18" r="2"/><circle cx="22" cy="9" r="3.5"/><circle cx="25" cy="19" r="2.5"/><path d="M4 8a9 9 0 0 1 9-5M29 4l-1 4-4-1"/></svg>
  </div>
  <h3 class="heading card__title">Operations</h3>
  <p class="card__desc">Operational workflows reside on a separate platform built for execution and recordkeeping.</p>
  <div class="card__rule"></div>
  <ul class="card__list">
    <li>Manages process execution and audit events</li>
    <li>Operates under separate terms and policies</li>
    <li>Not governed or administered on this site</li>
  </ul>
  <div class="card__mark"><span></span>The Copper Lantern</div>
</article>

<article class="card" style="left:775px">
  <div class="card__icon">
    <svg width="30" height="30" viewBox="0 0 30 30" fill="none" stroke="#8f8cf2" stroke-width="1.3"><rect x="4" y="4" width="20" height="20" rx="1"/><rect x="7" y="7" width="6" height="5"/><path d="M15 8h6M15 11h6M7 15h14M7 18h10M7 21h8"/><circle cx="24" cy="23" r="3.5"/></svg>
  </div>
  <h3 class="heading card__title">Project execution</h3>
  <p class="card__desc">Assets and execution sit at the project level within initiative-specific, ring-fenced structures.</p>
  <div class="card__rule"></div>
  <ul class="card__list">
    <li>Execution and delivery occur at the project level</li>
    <li>Ring-fenced, project-specific structures</li>
    <li>Outcomes vary by initiative</li>
  </ul>
  <div class="card__mark"><span></span>The Copper Lantern</div>
</article>

<!-- Ecosystem -->
<h2 class="heading eco__title abs center">How the ecosystem <span class="accent">works</span></h2>
<p class="copy eco__lead abs center">The ecosystem is designed around clear separation of responsibilities. Governance activities belong at the framework layer. Operational workflows, where available, belong on a separate operating platform designed for process execution and recordkeeping.</p>

<svg class="abs" style="top:1300px;left:0" width="1200" height="130" viewBox="0 0 1200 130" aria-hidden="true">
  <defs>
    <linearGradient id="stepRing" x1="0" y1="0" x2="1" y2="1">
      <stop offset="0" stop-color="#2ec3f0"/>
      <stop offset="1" stop-color="#8c5cf0"/>
    </linearGradient>
  </defs>
  <path d="M360 52 Q440 -10 520 57" fill="none" stroke="#a88ef5" stroke-width="1.2" stroke-dasharray="4 4"/>
  <path d="M680 88 Q760 150 838 90" fill="none" stroke="#a88ef5" stroke-width="1.2" stroke-dasharray="4 4"/>
  <circle cx="276" cy="65" r="52" fill="#fff" stroke="url(#stepRing)" stroke-width="2"/>
  <circle cx="602" cy="65" r="52" fill="#fff" stroke="url(#stepRing)" stroke-width="2"/>
  <circle cx="911" cy="65" r="52" fill="#fff" stroke="url(#stepRing)" stroke-width="2"/>
  <g fill="none" stroke="#8f8cf2" stroke-width="1.6">
    <path d="M252 55L276 41l24 14z"/><circle cx="276" cy="49" r="3"/>
    <path d="M254 58h44M259 60v20M267 60v20M276 60v20M285 60v20M293 60v20M252 82h48M250 87h52"/>
    <circle cx="594" cy="74" r="11"/><circle cx="594" cy="74" r="4"/>
    <circle cx="617" cy="54" r="7"/><circle cx="622" cy="72" r="5"/>
    <path d="M578 58a16 16 0 0 1 14-8M632 44l-2 7-6-2"/>
    <rect x="889" y="42" width="38" height="42" rx="1"/><rect x="894" y="47" width="11" height="9"/>
    <path d="M909 49h13M909 54h13M894 61h28M894 66h24M894 71h20M894 76h16"/>
    <circle cx="928" cy="80" r="7"/>
  </g>
</svg>

<div class="step" style="top:1440px;left:146px">
  <h3 class="heading step__title">Governance</h3>
  <p class="step__desc">Defines standards, explains role boundaries, and publishes framework information.</p>
</div>
<div class="step" style="top:1440px;left:472px">
  <h3 class="heading step__title">Operations</h3>
  <p class="step__desc">Manages workflow processes such as documentation steps and record-anchored audit events through a separate platform.</p>
</div>
<div class="step" style="top:1437px;left:781px">
  <h3 class="heading step__title">Project execution</h3>
  <p class="step__desc">Occurs at the project level through dedicated structures that hold responsibilities and assets where applicable.</p>
</div>

<!-- Escrow -->
<div class="escrow-bg abs"></div>
<h2 class="heading escrow__title abs">Independent escrow and<br>milestone <span class="accent">oversight</span></h2>
<p class="copy escrow__copy abs">Some initiatives use independent escrow arrangements to coordinate staged releases linked to milestone completion. Escrow can support execution discipline by requiring defined evidence before releases occur. Escrow does not guarantee outcomes, timelines, or success, and it is not administered by this website operator. This site describes the concept for clarity and transparency.</p>

<aside class="overview__frame abs">
  <div class="heading overview__head">Conceptual overview</div>
  <div class="overview__row">
    <div class="overview__icon">
      <svg width="22" height="22" viewBox="0 0 22 22" fill="none" stroke="#8f8cf2" stroke-width="1.2"><rect x="3" y="10" width="16" height="9" rx="1"/><circle cx="11" cy="6" r="3"/><path d="M7 14h8"/></svg>
    </div>
    <div>
      <div class="overview__label">Escrow</div>
      <p class="overview__text">Independent third-party holding with releases tied to predefined conditions.<br>Not administered by this website.</p>
    </div>
  </div>
  <div class="overview__row">
    <div class="overview__icon">
      <svg width="22" height="22" viewBox="0 0 22 22" fill="none" stroke="#8f8cf2" stroke-width="1.2"><circle cx="5" cy="6" r="2"/><path d="M7 6h8a3 3 0 0 1 0 6H7a3 3 0 0 0 0 6h8"/><path d="M15 16l2 2-2 2"/></svg>
    </div>
    <div>
      <div class="overview__label">Milestone Oversight</div>
      <p class="overview__text">Independent verification of predefined conditions; ensures accountability<br>but is not managed by this website.</p>
    </div>
  </div>
</aside>

<!-- Workflow -->
<div class="workflow__media abs" role="img" aria-label="Photo of a business team standing by a meeting table in front of a wall of workflow charts"></div>
<h2 class="heading workflow__title abs">Where operational<br>workflows <span class="accent">happen</span></h2>
<p class="copy workflow__copy abs">Operational workflows, including any onboarding or workflow participation where permitted, occur on a separate operating platform under separate terms and policies. If you need operational access, use the Brightmoor page on this site to navigate externally. This website does not host those workflows.</p>
<a class="btn btn--dark" href="#" style="top:2072px;left:611px;width:173px">Continue to Brightmoor
  <span class="btn__arrow"><svg width="10" height="10" viewBox="0 0 10 10"><path d="M1 5h7M5 2l3 3-3 3" stroke="#fff" stroke-width="1.4" fill="none" stroke-linecap="round"/></svg></span>
</a>

<!-- Contact -->
<section class="contact abs"></section>
<h2 class="heading contact__title abs center">Contact and <span class="accent">inquiries</span></h2>
<p class="copy contact__lead abs center">If you have questions about governance framework concepts, role boundaries, or information published on this website, you can contact the team using the Contact page. Do not submit sensitive personal data through public forms.</p>
<a class="btn btn--light" href="#" style="top:2336px;left:530px;width:140px">Contact the Team
  <span class="btn__arrow"><svg width="10" height="10" viewBox="0 0 10 10"><path d="M1 5h7M5 2l3 3-3 3" stroke="#fff" stroke-width="1.4" fill="none" stroke-linecap="round"/></svg></span>
</a>

<!-- Footer -->
<footer class="footer abs"></footer>
<div class="brand abs" style="top:2483px;left:114px;font-size:15px">
  <span class="brand__dot"></span>The Copper Lantern
</div>
<p class="footer__about abs">Informational governance content only. No operations, escrow, custody, or transactions.</p>

<div class="footer__col" style="left:395px">
  <h4>Navigaton</h4>
  <a href="#">Framework</a><a href="#">Projects</a><a href="#">Brightmoor</a><a href="#">Insights</a><a href="#">Company</a><a href="#">Contact</a><a href="#">Legal</a><a href="#">Glossary</a>
</div>
<div class="footer__col" style="left:572px">
  <h4>Framework</h4>
  <a href="#">Role Boundaries</a><a href="#">SPV Structure</a><a href="#">Escrow Model</a><a href="#">Records and Registers</a><a href="#">Risk and Boundaries</a>
</div>
<div class="footer__col" style="left:776px">
  <h4>Company</h4>
  <a href="#">About</a><a href="#">Leadership</a><a href="#">Governance</a><a href="#">Press</a><a href="#">Careers</a><a href="#">Contact</a>
</div>
<div class="footer__col" style="left:937px">
  <h4>Legal</h4>
  <a href="#">Terms of Use</a><a href="#">Privacy Policy</a><a href="#">Cookie Policy</a><a href="#">Disclaimer &amp; Risk Notices</a><a href="#">Acceptable Use Policy</a><a href="#">Accessibility Statement</a>
</div>

<div class="footer__rule abs"></div>
<p class="footer__legal abs" style="top:2716px">© 2026 The Copper Lantern. All rights reserved.</p>
<p class="footer__legal abs" style="top:2740px">This website is provided for general informational purposes only. Nothing on this site is an offer, solicitation, or professional advice.</p>

</body>
</html>
```